Homepage design competition to choose a designer for $1500 full website for a Small Animal Veterinar

We are running a homepage design competition to choose a designer who will later code an entire website. Please note, this competition is only for the front page design. There will be an additional payment of $1500 (Australian $AUD) for the complete website design including coding payment.

Front Page: First we need a front page design for our companion animal veterinary hospital. I will use the frontpage design competition to choose a designer for the full website.
Marlow Vet Clinic is a companion animal veterinary hospital in Singleton NSW. We provide veterinary medical and surgical treatment for dogs, cats, rabbits, birds and reptiles. Mostly dogs and cats.
Our reception is a 120 year old church and the hospital is 6 years old and custom built.
I want the site to be amazing. The sort of thing that could win prizes. The front page should be simple, fun and engaging whilst maintaining a strong sense of professionalism. Simple and elegant visual effects with subtle movement. The winning design will show originality.
Our main demographic is women aged 25 to 44 years old. We are a coal mining town. Most of our money comes from coal miners wives.
The front page must display our phone number and link to our facebook page. Otherwise the front page can have anything. The front page should impress new clients and reassure existing clients.
We pride ourselves on following up everything and caring for pets and their people their entire life. Please see our existing (horrible) website for more details about our business. http://www.marlowvetclinic.example/
Incorporate only amazing things from the old website. I hate the old website, so there is probably not much to use. We need something new and amazing.
Fully responsive design.

Characters: We have a logo and animal characters to incorporate into the design. These characters will be used throughout our email and facebook advertising. If they could be used with some movement and sound effects, that would be cool, but nothing too childish or silly.

Live site: please include links to live demo sites if possible.
Please include links to your other work.

Full Website: The successful designer of the frontpage must be able to demonstrate the ability produce a full website. The full website designer will be commissioned after the front page is chosen. We have budgeted for a full website of $1500.
I need to be able to add new articles to the website that will link from email newsletters and facebook, so the full website will need to be something I can modify or add to.
I have a working knowledge of Joomla, Wordpress and html.
The full website will have map, history of the hospital, history of the chapel, links to local services, pet care advice, memorials.
Ideally the winning designer will be able to integrate appointments available with our existing veterinary management software.
Fully responsive design.

Here are some websites that I like:
https://drbexley.example.au/
http://quincepepper.example/
http://www.xn--dorotawelnicka-abc12k.example/
https://www.zov.example.au/
https://www.frisko.example.au/
https://topmowers.example.au/
https://www.redgatecider.example/

Target Market(s)

Women aged 25 to 44 years

Industry/Entity Type

Veterinary

Number of Pages Required

1 page

Font styles to use
Serif
Sans Serif

Requirements
Must have
• Phone number
• Facebook Link https://www.facebook.com/marlow.vetclinic?v=wall
• Simplicity
• Originality
• Animal characters-images attached
Nice to have
• Images
• Clean
• Link to live site.
• Links to your other work.
• Demonstrate ability to integrate appointment booking with our veterinary software
Should not have
• Heaps of words
• Complexity

```html
<!DOCTYPE html>
<html lang="en">
<head>
<meta charset="utf-8">
<title>Marlow Vet Clinic</title>
<link href="https://fonts.googleapis.com/css2?family=Signika:wght@300;400;600&family=Lato:ital,wght@1,300;1,700&display=swap" rel="stylesheet">
<style>
:root{
  --pink:#e01a6e;
  --pink-soft:#e8609a;
  --peach:#fde5b4;
  --ink:#3a3a3a;
  --muted:#8a8a8a;
  --nav:#efefef;
  --line:#e2e2e2;
  --tile-1:#ef9aa5;
  --tile-2:#c496c9;
  --tile-3:#a699c6;
  --tile-4:#98aee2;
  --tile-5:#8ec8ee;
  --white:#ffffff;
}
*{margin:0;padding:0;box-sizing:border-box}
html,body{width:1200px;height:2169px;overflow:hidden;background:var(--white)}
body{position:relative;font-family:"Signika",sans-serif;color:var(--ink)}
a{color:inherit;text-decoration:none}
.backdrop{
  position:absolute;left:32px;top:29px;width:1136px;height:2111px;
  background:
    repeating-linear-gradient(180deg,rgba(255,255,255,0) 0 44px,rgba(255,255,255,.04) 44px 88px),
    linear-gradient(180deg,var(--pink) 0%,#e8557f 35%,#f39a93 60%,#f8c8a4 82%,var(--peach) 100%);
}
.brand-rule{position:absolute;top:159px;height:1px;background:rgba(255,255,255,.45)}
.brand-rule.left{left:341px;width:171px}
.brand-rule.right{left:690px;width:169px}
.brand{
  position:absolute;left:519px;top:77px;width:162px;height:162px;
  border:3px solid var(--white);display:flex;flex-direction:column;
  align-items:center;justify-content:center;color:var(--white);
  font-weight:600;font-size:24px;line-height:1.1;text-align:center;
}
.address{position:absolute;top:262px;left:0;width:1200px;text-align:center;color:var(--white);font-size:14px;font-weight:600}
.phone{position:absolute;top:284px;left:0;width:1200px;text-align:center;color:var(--white);font-size:21px;font-weight:600}
.social-link{position:absolute;left:582px;top:320px;width:36px;height:36px;border-radius:50%;background:var(--white)}
.card{position:absolute;left:153px;top:388px;width:893px;height:1524px;background:var(--white);border-radius:5px;overflow:hidden}
.nav{height:65px;background:var(--nav);border-bottom:1px solid var(--line);position:relative;font-size:14px;font-weight:400}
.nav a{position:absolute;top:0;line-height:65px;transform:translateX(-50%);white-space:nowrap}
.nav a.current{top:17px;line-height:35px;width:71px;text-align:center;background:var(--white);border:1px solid var(--line);color:var(--pink);transform:none}
.hero{position:absolute;top:65px;left:0;width:893px;height:472px;
  background:linear-gradient(90deg,#6d6d6d 0%,#9a9a9a 30%,#cfcfcf 55%,#ededed 75%,#f6f6f6 100%)}
.hero-photo{position:absolute;left:0;top:0;width:560px;height:472px}
.quote{position:absolute;left:600px;top:130px;width:360px;transform:translateX(-50%);margin-left:80px;
  font-family:"Lato",sans-serif;font-style:italic;font-weight:300;font-size:27px;line-height:39px;text-align:center;color:#333}
.quote strong{font-weight:700}
.dots{position:absolute;top:444px;left:421px;display:flex;gap:7px}
.dots span{width:10px;height:10px;border-radius:50%;background:#444}
.dots span.active{background:var(--pink)}
.intro{position:absolute;top:580px;left:0;width:893px;text-align:center;color:var(--pink);font-weight:300;font-size:26px;line-height:34px}
.hours{position:absolute;top:711px;left:0;width:893px;text-align:center;font-size:14px;line-height:19px;font-weight:300}
.btn{position:absolute;left:336px;width:222px;height:64px;border-radius:5px;font-size:18px;font-weight:300;display:flex;align-items:center;justify-content:center}
.btn.primary{top:777px;background:var(--pink-soft);color:var(--white)}
.btn.secondary{top:1412px;background:var(--nav);border:1px solid var(--line);color:#555}
.divider{position:absolute;top:887px;left:78px;width:736px;height:1px;background:var(--line)}
.section-title{position:absolute;top:920px;left:0;width:893px;text-align:center;color:var(--pink);font-weight:300;font-size:26px}
.section-lead{position:absolute;top:982px;left:0;width:893px;text-align:center;font-size:15px;line-height:19px;font-weight:300}
.services{position:absolute;top:1055px;left:97px;width:699px;height:119px;display:flex;border-radius:3px;overflow:hidden}
.service{flex:1;color:var(--white);display:flex;flex-direction:column;align-items:center;justify-content:flex-end;padding-bottom:12px;font-size:14px;font-weight:600}
.service svg{margin-bottom:12px}
.service:nth-child(1){background:var(--tile-1)}
.service:nth-child(2){background:var(--tile-2)}
.service:nth-child(3){background:var(--tile-3)}
.service:nth-child(4){background:var(--tile-4)}
.service:nth-child(5){background:var(--tile-5)}
.copy{position:absolute;top:1221px;width:330px;font-size:14px;line-height:17.6px;text-align:justify;font-weight:300}
.copy.left{left:97px}
.copy.right{left:467px}
.footer{position:absolute;top:1955px;font-size:11.5px;line-height:14.5px;color:var(--muted);font-weight:300}
.footer h3{font-size:14px;font-weight:400;color:#6e6e6e;margin-bottom:12px}
.footer.about{left:250px;width:332px;text-align:justify}
.footer.contact{left:620px;width:330px}
.social{display:flex;gap:9px;margin-top:8px}
.social span{width:28px;height:28px;border-radius:50%;background:var(--muted)}
</style>
</head>
<body>
<div class="backdrop"></div>
<div class="brand-rule left"></div>
<div class="brand-rule right"></div>
<div class="brand">Marlow<br>Vet Clinic</div>
<p class="address">27 Orchard CL, Singleton Heights, NSW 2330.</p>
<p class="phone">02 5550 1927</p>
<a class="social-link" href="#" aria-label="Social page"></a>

<main class="card">
  <nav class="nav">
    <a class="current" href="#" style="left:67px">Home</a>
    <a href="#" style="left:210px">Appointments</a>
    <a href="#" style="left:329px">Services</a>
    <a href="#" style="left:453px">Pet Care Advice</a>
    <a href="#" style="left:583px">Memorials</a>
    <a href="#" style="left:678px">Blog</a>
    <a href="#" style="left:775px">Contact Us</a>
  </nav>
  <section class="hero">
    <div class="hero-photo" role="img" aria-label="Black and white photo of a mother and daughter smiling with their small dog"></div>
    <blockquote class="quote">“A small animal vet<br>is what I was looking for<br>and for all you have done<br>for my Dog so far<br><strong>THANKYOU!</strong><br>she is a happy girl now."</blockquote>
    <div class="dots"><span class="active"></span><span></span><span></span><span></span></div>
  </section>
  <h1 class="intro">We are a Companion Animal Veterinary Hospital in Singleton<br>committed to providing excellent care for loved pets<br>and their owners.</h1>
  <p class="hours">Open on Weekdays: 8.30am to 5.30pm &amp;<br>Saturday: 9.00am to 12.00pm</p>
  <a class="btn primary" href="#">Book an Appointment</a>
  <div class="divider"></div>
  <h2 class="section-title">Services we offer</h2>
  <p class="section-lead">We pride ourselves on following up everything and caring for pets and their people their entire life.<br>We provide veterinary medical and surgical treatment for dogs, cats, rabbits, birds and reptiles.</p>
  <div class="services">
    <div class="service">
      <svg width="50" height="50" viewBox="0 0 50 50" fill="none" stroke="#fff" stroke-width="2"><ellipse cx="25" cy="32" rx="9" ry="8"/><circle cx="13" cy="20" r="4"/><circle cx="21" cy="13" r="4"/><circle cx="29" cy="13" r="4"/><circle cx="37" cy="20" r="4"/></svg>
      Schooling</div>
    <div class="service">
      <svg width="50" height="50" viewBox="0 0 50 50" fill="none" stroke="#fff" stroke-width="2"><rect x="16" y="14" width="10" height="24" transform="rotate(45 21 26)"/><line x1="10" y1="40" x2="4" y2="46"/><line x1="33" y1="17" x2="41" y2="9"/><line x1="37" y1="5" x2="45" y2="13"/></svg>
      Vaccinations</div>
    <div class="service">
      <svg width="50" height="50" viewBox="0 0 50 50" fill="none" stroke="#fff" stroke-width="2"><circle cx="37" cy="11" r="5"/><circle cx="41" cy="22" r="5"/><line x1="33" y1="15" x2="8" y2="42"/><line x1="37" y1="22" x2="12" y2="38"/></svg>
      Surgery</div>
    <div class="service">
      <svg width="50" height="50" viewBox="0 0 50 50" fill="none" stroke="#fff" stroke-width="2"><path d="M8 12h34v20H22l-8 8v-8H8z"/></svg>
      Behaviour Consults</div>
    <div class="service">
      <svg width="50" height="50" viewBox="0 0 50 50" fill="none" stroke="#fff" stroke-width="2"><path d="M25 42 8 25a9 9 0 0 1 17-11 9 9 0 0 1 17 11z"/></svg>
      Grieving Support</div>
  </div>
  <p class="copy left">Lorem ipsum dolor sit amet, consectetur adipiscing elit. Quisque sed urna eget metus pellentesque semper. Aliquam sollicitudin nisi nulla, id bibendum nibh placerat et. Vivamus in feugiat lacus, ut luctus massa. Cras egestas tempus venenatis. Suspendisse felis augue, pellentesque nec justo nec, consequat maximus ex. Proin feugiat egestas vehicula.</p>
  <p class="copy right">Vestibulum sed neque sed ante vulputate fermentum vel id libero. Donec tempus, felis bibendum sollicitudin vestibulum, est quam blandit justo, a bibendum sapien sapien feugiat eros. Aliquam ex est, rutrum id ligula at, accumsan dapibus erat. Curabitur ex arcu, dignissim eu eros eget, aliquet imperdiet massa. Sed eget sapien sit amet lectus sollicitudin suscipit sit amet quis dui.</p>
  <a class="btn secondary" href="#">Learn More</a>
</main>

<footer>
  <div class="footer about">
    <h3>About Us</h3>
    <p>Lorem ipsum Quisque sed urna eget metus pellentesque semper. Aliquam sollicitudin nisi nulla, id bibendum nibh placerat et. Vivamus in feugiat lacus, ut luctus massa. Cras egestas tempus venenatis. Curabitur ex arcu, dignissim eu eros eget, aliquet imperdiet massa.</p>
  </div>
  <div class="footer contact">
    <h3>Get in touch</h3>
    <p>Address: 27 Orchard CL, Singleton Heights, NSW 2330.<br>Phone: 02 5550 1927<br>Email: info@marlowvetclinic.example</p>
    <div class="social"><span aria-label="Social link one"></span><span aria-label="Social link two"></span><span aria-label="Social link three"></span><span aria-label="Social link four"></span></div>
  </div>
</footer>
</body>
</html>
```